Manifesto

I want a manifesto with the following five manifestos for our Not for Profit

- We are a For-purpose organisation
- Every service we offer is free
- Every product we sell funds our services
- Every financial transaction is transparent
- Our service is for the greater good
- Our purpose is always to serve the people
- We are a for purpose organisation

Its to go with this website logo/look/feel www.brightlantern.co.nz

Two attachments:

1. I quite like this look/feel of a manifesto (see attached), I want something clean, professional but I also quite like either Retro modern look feel also like a fresh, and uplifting as its for sick people coming to see us and our funds where anyone buys a product are used for helping those who are sick with healing......so needs something conveyed that is fresh, uplifing yet professional.
2. This attachment is how I wrote this down when inspired of how I wanted Bright Lantern to operate. This is our values chart. It has to say

Also check out our website for our logo, look etc.. it doesnt have to be the same but red somewhere would link back to logo. www.brightlantern.co.nz .

Industry/Entity Type

Financial

```html
<!DOCTYPE html>
<html lang="en">
<head>
<meta charset="utf-8">
<title>Bright Lantern Manifesto</title>
<link rel="stylesheet" href="https://fonts.googleapis.com/css2?family=Arvo:ital,wght@0,400;0,700;1,700&family=Lobster&display=swap">
<style>
  :root {
    --backdrop: #ececec;
    --paper-light: #d5dbe2;
    --paper-mid: #c3cad3;
    --paper-dark: #b4bcc6;
    --ink: #353535;
    --red: #c41230;
    --lift: rgba(255,255,255,0.55);
    --slab: "Arvo", "Rockwell", serif;
    --script: "Lobster", cursive;
  }
  * { margin: 0; padding: 0; box-sizing: border-box; }
  html, body {
    width: 1200px; height: 1000px; overflow: hidden;
    background: var(--backdrop);
  }
  .poster {
    position: absolute; left: 275px; top: 52px;
    width: 635px; height: 900px;
    background:
      radial-gradient(ellipse at 30% 20%, var(--paper-light), transparent 60%),
      radial-gradient(ellipse at 75% 75%, var(--paper-dark), transparent 65%),
      var(--paper-mid);
  }
  .line {
    position: absolute; white-space: nowrap; line-height: 1;
    text-shadow: 1px 2px 1px var(--lift);
  }
  .slab { font-family: var(--slab); font-weight: 700; }
  .script { font-family: var(--script); font-weight: 400; }
  .ink { color: var(--ink); }
  .red { color: var(--red); }
  .left { left: 23px; }
  .full { left: 23px; width: 588px; text-align: center; }
  .right-col { left: 372px; width: 239px; text-align: center; }
  .right-col-wide { left: 338px; width: 273px; text-align: right; }
  .divider { position: absolute; left: 23px; width: 588px; height: 10px; }
  .divider path { fill: none; stroke: var(--ink); stroke-width: 2; stroke-linecap: round; }
</style>
</head>
<body>
<main class="poster" aria-label="Bright Lantern manifesto poster">

  <!-- Statement 1 -->
  <p class="line slab ink left" style="top:30px;font-size:47px;letter-spacing:0.5px;">WE ARE A</p>
  <p class="line slab red left" style="top:84px;font-size:38px;">FOR PURPOSE</p>
  <p class="line slab red left" style="top:128px;font-size:33.5px;">ORGANISATION</p>

  <p class="line script red right-col" style="top:28px;font-size:39px;">Every Service</p>
  <p class="line slab ink right-col" style="top:73px;font-size:21px;letter-spacing:4px;">we offer is</p>
  <p class="line slab ink right-col" style="top:95px;font-size:74px;letter-spacing:6px;">FREE</p>

  <svg class="divider" style="top:176px;" viewBox="0 0 588 10" preserveAspectRatio="none" aria-hidden="true"><path d="M2 6 Q150 1 294 4 T586 5"/></svg>

  <!-- Statement 2 -->
  <p class="line slab red full" style="top:200px;font-size:60px;">EVERY PRODUCT</p>
  <p class="line slab ink full" style="top:264px;font-size:33px;letter-spacing:0.5px;">we sell funds our services</p>

  <svg class="divider" style="top:310px;" viewBox="0 0 588 10" preserveAspectRatio="none" aria-hidden="true"><path d="M2 4 Q160 8 300 5 T586 4"/></svg>

  <!-- Statement 3 -->
  <p class="line slab red left" style="top:343px;font-size:50px;letter-spacing:10px;">EVERY</p>
  <p class="line slab red left" style="top:401px;font-size:30px;letter-spacing:6px;">FINANCIAL</p>
  <p class="line slab ink left" style="top:438px;font-size:25px;letter-spacing:4.5px;">TRANSACTION</p>
  <p class="line slab ink left" style="top:469px;font-size:23px;letter-spacing:4px;">is transparent</p>

  <p class="line slab ink right-col-wide" style="top:346px;font-size:23px;letter-spacing:2.5px;">OUR SERVICE IS</p>
  <p class="line script red right-col-wide" style="top:376px;font-size:40px;">for the greater</p>
  <p class="line slab red right-col-wide" style="top:424px;font-size:68px;">GOOD</p>

  <svg class="divider" style="top:512px;" viewBox="0 0 588 10" preserveAspectRatio="none" aria-hidden="true"><path d="M2 5 Q140 2 300 5 T586 6"/></svg>

  <!-- Statement 4 -->
  <p class="line slab ink full" style="top:545px;font-size:48px;letter-spacing:5px;">OUR PURPOSE IS</p>
  <p class="line script red full" style="top:598px;font-size:47px;">always to serve the people</p>

  <svg class="divider" style="top:672px;" viewBox="0 0 588 10" preserveAspectRatio="none" aria-hidden="true"><path d="M2 6 Q160 2 294 5 T586 4"/></svg>

  <!-- Statement 5 -->
  <p class="line slab ink full" style="top:700px;font-size:38px;letter-spacing:2.5px;">WE ARE A FOR PURPOSE</p>
  <p class="line script red full" style="top:738px;font-size:104px;">organisation</p>

  <p class="line slab ink full" style="top:846px;font-size:15px;font-style:italic;">Bright Lantern Manifesto</p>
  <p class="line ink full" style="top:871px;font-family:var(--slab);font-size:13px;letter-spacing:2.5px;">www.brightlantern.co.nz</p>

</main>
</body>
</html>
```